National online rug retailer needs a home page design

See the LoomNest logo and create a home page design around that color theme. Details are spelled out in word document uploaded below.
Updates

Apparently this website did not take my attachement showing the logo and basic requirements.  If you would send me your email address, I will send you the attachment directly.
Best regards,
Ned Carver
ncarver@qwplex.com

Target Market(s)

The target market is home owners 25 to 75 years old with combined incomes over $100,000 per year.

Industry/Entity Type

Online

Requirements
Must have
• Lots of white space with black letters and creative use of red and possibly one other color. Would like a compelling call to action button.

```html
<!DOCTYPE html>
<html lang="en">
<head>
<meta charset="utf-8">
<title>LoomNest – Home</title>
<link href="https://fonts.googleapis.com/css2?family=Arimo:wght@400;700&display=swap" rel="stylesheet">
<style>
:root{
  --red:#d7151b;
  --red-dark:#b80f14;
  --ink:#333;
  --grey-bg:#e8e8e8;
  --panel:#e1e1e1;
  --band:#5f5f5f;
  --footer:#4a4a4a;
  --white:#fff;
  --muted:#666;
}
*{margin:0;padding:0;box-sizing:border-box}
html,body{width:1157px;height:1200px;overflow:hidden}
body{background:var(--grey-bg);font-family:"Arimo",Arial,sans-serif;color:var(--ink);position:relative}
.abs{position:absolute}
.header-bg{left:0;top:0;width:1157px;height:86px;background:linear-gradient(#fff,#f1f1f1)}
.band{left:0;top:86px;width:1157px;height:24px;background:linear-gradient(#4e4e4e,#777)}
.page{left:241px;top:110px;width:674px;height:824px;background:var(--white)}
.logo{left:240px;top:16px;display:flex;align-items:center;gap:5px}
.logo-mark{width:16px;height:16px;background:var(--red)}
.logo-name{font-size:28px;font-weight:400;color:var(--red);letter-spacing:-.5px}
.tagline{left:297px;top:54px;font-size:7px;color:var(--muted)}
.search{left:482px;top:30px;display:flex;height:16px}
.search-field{width:151px;border:1px solid #bbb;background:#fff;font-size:8px;color:#555;padding:2px 6px;line-height:11px}
.search-btn{width:44px;background:var(--red);color:#fff;font-size:8px;text-align:center;line-height:16px}
.cart{left:742px;top:18px;font-size:7px;color:#444;word-spacing:1px}
.phone{left:742px;top:30px;font-size:10px;font-weight:700;color:var(--red)}
.account{left:742px;top:47px;font-size:7px;color:#444}
.chat{left:818px;top:47px;width:97px;height:9px;background:var(--red);color:#fff;font-size:6px;font-weight:700;display:flex;justify-content:space-around;align-items:center}
.nav{left:241px;top:74px;width:674px;height:27px;display:flex;background:var(--red)}
.nav a{color:#fff;text-decoration:none;font-size:10px;display:flex;align-items:center;justify-content:center;border-right:1px solid #e8585c}
.nav a.current{background:var(--red-dark);font-weight:700}
.sidebar{left:246px;top:120px;width:118px}
.sidebar h2{font-size:15px;color:var(--red);padding:2px 5px 5px;border-bottom:1px solid #ddd}
.group{padding:4px 5px 6px;border-bottom:1px solid #ddd}
.group .head{font-size:9px;font-weight:700;color:var(--red);line-height:12px}
.group .sub{font-size:9px;color:#444;line-height:12px;padding-left:6px}
.group .leaf{font-size:8px;color:#666;line-height:12px;padding-left:22px}
.group .more{font-size:8px;color:var(--red);font-weight:700;line-height:14px;display:flex;align-items:center;gap:3px}
.plus{width:8px;height:8px;background:var(--red);color:#fff;font-size:8px;line-height:8px;text-align:center}
.filters{padding:6px 5px 10px;border-bottom:1px solid #ddd}
.filters div{font-size:9.5px;font-weight:700;color:var(--red);line-height:16px}
.social{left:246px;top:518px;width:118px;height:103px;background:#2b4a8c;color:#fff}
.social .side{position:absolute;left:0;top:0;width:36px;height:103px;background:linear-gradient(90deg,#e6e6e6,#8a93a8)}
.social .note{position:absolute;left:40px;top:6px;font-size:7px;font-weight:700;line-height:9px;width:76px}
.social .big{position:absolute;left:38px;top:40px;font-size:24px;font-weight:700}
.social .follow{position:absolute;left:38px;top:64px;font-size:9px;font-weight:700}
.social .btn{position:absolute;left:38px;top:80px;width:58px;height:14px;background:#fff;color:#2b4a8c;font-size:8px;font-weight:700;text-align:center;line-height:14px}
.panel{left:367px;top:206px;width:407px;height:714px;background:var(--panel)}
.banner{left:367px;top:119px;width:407px;height:85px;background:linear-gradient(90deg,#3f8aa5 0%,#b7a27b 60%,#d68a3a 100%);color:#fff}
.banner .strip1{position:absolute;left:0;top:28px;width:407px;height:22px;background:rgba(200,30,40,.85)}
.banner .strip2{position:absolute;left:0;top:56px;width:407px;height:29px;background:rgba(40,20,20,.8)}
.banner .t1{position:absolute;left:6px;top:6px;font-size:17px;letter-spacing:.3px}
.banner .t2{position:absolute;left:6px;top:31px;font-size:17px;font-weight:700}
.banner .t2 small{font-size:9px;margin-left:4px}
.banner .t3{position:absolute;left:6px;top:63px;font-size:12px;font-weight:700}
.banner .t3 small{font-size:6px;margin-left:3px}
.tile{position:absolute;width:126px;height:155px;background:#fff}
.tile .rule{position:absolute;left:5px;width:116px;height:1px;background:#ddd}
.tile .rule.t{top:8px}.tile .rule.b{bottom:8px}
.tile .art{position:absolute;left:15px;top:18px;width:95px;height:95px;border:1px solid #ccc}
.tile .label{position:absolute;left:0;width:126px;top:125px;text-align:center;font-size:10px;font-weight:700;color:#444;letter-spacing:.3px}
.persian{background:radial-gradient(circle,#f3d57a 20%,#d94a30 60%,#b5352a)}
.kilim{background:linear-gradient(135deg,#2b3e8a,#c63a2c 50%,#2b3e8a)}
.modern{background:linear-gradient(#b5410f,#e8771a 50%,#f6b23b)}
.ziegler{background:radial-gradient(circle,#d8563e 45%,#ecd7a9 90%)}
.shag{background:linear-gradient(135deg,#f35ca8,#d31e50 50%,#f599c6)}
.modern-cream{background:radial-gradient(circle,#d7b77d 15%,#efe0b6 60%)}
.section-title{left:377px;top:708px;font-size:15px;font-weight:700;color:#555}
.promo{position:absolute;left:778px;width:130px}
.like-box{top:119px;height:131px;background:linear-gradient(135deg,#555 45%,#b98548 70%,#6fa14a)}
.like-box span{position:absolute;left:4px;top:4px;color:#fff;font-size:20px;line-height:20px;letter-spacing:-.5px}
.like-box span b{font-weight:700}
.red-box{background:var(--red);color:#fff;text-align:center}
.hey{top:258px;height:96px}
.hey .h{font-size:32px;font-weight:700;margin-top:6px;letter-spacing:-1px}
.hey .s{font-size:14px;line-height:16px;letter-spacing:-.5px}
.help{top:362px;height:100px}
.help .h{font-size:18px;font-weight:700;margin-top:11px;letter-spacing:-.5px}
.help .s{font-size:14px;line-height:17px;letter-spacing:-.5px}
.help .s b{display:block}
.grey-box{background:linear-gradient(#f2f2f2,#dcdcdc);overflow:hidden}
.grey-box .h{position:absolute;left:6px;top:6px;font-size:16px;font-weight:700;color:var(--red);letter-spacing:-.6px;line-height:16px;white-space:nowrap}
.grey-box .s{position:absolute;left:7px;font-size:9px;color:#444;line-height:11px}
.uk{top:469px;height:73px}
.price{top:548px;height:100px}
.money{top:655px;height:74px}
.seal{position:absolute;left:860px;top:697px;width:50px;height:50px;border-radius:50%;background:radial-gradient(circle,#f7d23a 45%,#222 47%,#222 58%,#e8b51a 60%)}
.footer{left:241px;top:934px;width:674px;height:220px;background:var(--footer);color:#fff}
.pay{position:absolute;left:173px;top:12px;display:flex;gap:2px}
.pay span{width:31px;height:20px;background:#f4f4f4;border:1px solid #ccc}
.col{position:absolute;top:53px}
.col h3{font-size:9.5px;font-weight:700;margin-bottom:5px}
.col div{font-size:7px;line-height:8.6px}
.bottom-nav{position:absolute;left:0;top:186px;width:674px;text-align:center;font-size:7.5px;word-spacing:2px}
.copy{position:absolute;left:0;top:202px;width:674px;text-align:center;font-size:7px}
</style>
</head>
<body>
<div class="abs header-bg"></div>
<div class="abs band"></div>
<div class="abs page"></div>

<div class="abs logo"><span class="logo-mark"></span><span class="logo-name">LoomNest.com</span></div>
<div class="abs tagline">for domestic and heirloom values</div>

<div class="abs search"><div class="search-field">enter key words or item #</div><div class="search-btn">Search</div></div>

<div class="abs cart">Items:___ I Total $0.00 &nbsp;I&nbsp; View Cart &nbsp;I&nbsp; Checkout &nbsp;I</div>
<div class="abs phone">Order toll - free : 1 - 888 - 555 - 0142</div>
<div class="abs account">My Account &nbsp;I&nbsp; Sign In</div>
<div class="abs chat"><span>LIVE CHAT</span><span>ONLINE</span></div>

<nav class="abs nav">
  <a class="current" style="width:60px">HOME</a>
  <a style="width:129px">SELECTION GUIDES</a>
  <a style="width:85px">RUG CARE</a>
  <a style="width:56px">FAQ</a>
  <a style="width:115px">RETURN POLICY</a>
  <a style="width:106px">FREE SHIPPING</a>
  <a style="width:123px;border:none">CLEARANCE RUGS</a>
</nav>

<aside class="abs sidebar">
  <h2>Categories</h2>
  <div class="group">
    <div class="head">⌄ Brown</div>
    <div class="sub">› Rug Theme</div>
    <div class="leaf">Traditional</div><div class="leaf">Transitional</div><div class="leaf">Casual</div>
    <div class="sub" style="margin-top:3px">› Colour Way</div>
    <div class="leaf">Black</div><div class="leaf">Blue</div><div class="leaf">Green</div><div class="leaf">Gold</div>
    <div class="more" style="margin-top:3px"><span class="plus">+</span>Show More</div>
  </div>
  <div class="group">
    <div class="head">⌄ Size</div>
    <div class="sub">› Rug Theme</div>
    <div class="leaf">Traditional</div><div class="leaf">Transitional</div><div class="leaf">Casual</div>
    <div class="more"><span class="plus">+</span>Show More</div>
  </div>
  <div class="filters">
    <div>› SIZE</div><div>› SHAPE</div><div>› FIBER CONTENT</div><div>› MFGR. BRAND</div><div>› MFGR.COLLECTION</div><div>› PRICE</div>
  </div>
</aside>

<div class="abs social">
  <div class="side"></div>
  <div class="note">Like LoomNest Direct for a Special Discount.</div>
  <div class="big">LIKE</div>
  <div class="follow">Follow us on</div>
  <div class="btn">Click Here</div>
</div>

<div class="abs panel"></div>
<div class="abs banner" role="img" aria-label="Stack of colourful rugs behind the summer sale message">
  <div class="strip1"></div><div class="strip2"></div>
  <div class="t1">SUMMER CLEARANCE OUTLET SALE</div>
  <div class="t2">EXTRA 10% OFF<small>Quantities Limited - Shop Now</small></div>
  <div class="t3">LoomNest Sumer Sweepstakes<small>Win A £500 Shopping Spree and Free Design Consulatation!</small></div>
</div>

<div class="tile" style="left:374px;top:218px"><div class="rule t"></div><div class="art persian" role="img" aria-label="Persian rug"></div><div class="label">Persian Rugs</div><div class="rule b"></div></div>
<div class="tile" style="left:507px;top:218px"><div class="rule t"></div><div class="art kilim" role="img" aria-label="Kilim rug"></div><div class="label">Kilim Rugs</div><div class="rule b"></div></div>
<div class="tile" style="left:640px;top:218px"><div class="rule t"></div><div class="art modern" role="img" aria-label="Modern orange rug"></div><div class="label">Modern Rugs</div><div class="rule b"></div></div>

<div class="tile" style="left:374px;top:381px"><div class="rule t"></div><div class="art ziegler" role="img" aria-label="Ziegler rug"></div><div class="label">Ziegler Rugs</div><div class="rule b"></div></div>
<div class="tile" style="left:507px;top:381px"><div class="rule t"></div><div class="art shag" role="img" aria-label="Pink shag rug"></div><div class="label">Shag Rugs</div><div class="rule b"></div></div>
<div class="tile" style="left:640px;top:381px"><div class="rule t"></div><div class="art modern-cream" role="img" aria-label="Cream patterned rug"></div><div class="label">Modern Rugs</div><div class="rule b"></div></div>

<div class="tile" style="left:374px;top:543px"><div class="rule t"></div><div class="art persian" role="img" aria-label="Persian rug"></div><div class="label">Persian Rugs</div><div class="rule b"></div></div>
<div class="tile" style="left:507px;top:543px"><div class="rule t"></div><div class="art kilim" role="img" aria-label="Kilim rug"></div><div class="label">Kilim Rugs</div><div class="rule b"></div></div>
<div class="tile" style="left:640px;top:543px"><div class="rule t"></div><div class="art modern" role="img" aria-label="Modern orange rug"></div><div class="label">Modern Rugs</div><div class="rule b"></div></div>

<div class="abs section-title">Discount Rugs</div>
<div class="tile" style="left:374px;top:734px"><div class="rule t"></div><div class="art persian" role="img" aria-label="Persian rug"></div><div class="label">Persian Rugs</div><div class="rule b"></div></div>
<div class="tile" style="left:507px;top:734px"><div class="rule t"></div><div class="art kilim" role="img" aria-label="Kilim rug"></div><div class="label">Kilim Rugs</div><div class="rule b"></div></div>
<div class="tile" style="left:640px;top:734px"><div class="rule t"></div><div class="art modern" role="img" aria-label="Modern orange rug"></div><div class="label">Modern Rugs</div><div class="rule b"></div></div>

<div class="promo like-box" role="img" aria-label="Fanned stack of colourful rugs"><span>YOU MAY<br>ALSO<br><b>LIKE</b></span></div>
<div class="promo red-box hey"><div class="h">HEY</div><div class="s">Will this be your<br>first order?</div></div>
<div class="promo red-box help"><div class="h">Need Help?</div><div class="s">Drop us a line We<br>are here to help<b>click to email</b></div></div>
<div class="promo grey-box uk" role="img" aria-label="White delivery van">
  <div class="h">FREE UK</div><div class="s" style="top:24px">Delivery Service</div>
</div>
<div class="promo grey-box price">
  <div class="h">PRICE PROMISE</div><div class="s" style="top:26px">We won't be beaten<br>on price</div>
  <svg style="position:absolute;left:62px;top:48px" width="64" height="56" viewBox="0 0 64 56" aria-hidden="true"><circle cx="34" cy="32" r="26" fill="none" stroke="#333" stroke-width="5"/></svg>
</div>
<div class="promo grey-box money">
  <div class="h">MONEY BACK<br>GUARANTEE</div><div class="s" style="top:42px">Peace of mind</div>
</div>
<div class="abs seal"></div>

<footer class="abs footer">
  <div class="pay"><span></span><span></span><span></span><span></span><span></span><span></span><span></span><span></span><span></span><span></span></div>
  <div class="col" style="left:129px"><h3>Customer Service</h3>
    <div>Shipping</div><div>Return Policy</div><div>Privacy Policy</div><div>Ordering &amp; Delivery Checklist</div><div>Terms of Use</div><div>Terms of Sale</div><div>Contact Us</div><div>Environmental Policy</div></div>
  <div class="col" style="left:297px"><h3>Resources</h3>
    <div>Product Articles</div><div>Learning Center</div><div>Help</div><div>Refer A Friend</div><div>LoomNest Blog</div><div>Room Scene Viewer</div><div>Site Map</div><div>FAQ</div><div>Customer Testimonials</div><div>Photo Gallery</div></div>
  <div class="col" style="left:458px"><h3>Corporate Info</h3>
    <div>About LoomNest.com</div><div>Careers</div><div>Affiliates</div></div>
  <div class="bottom-nav">HOME &nbsp;I&nbsp; SELECTION GUIDES &nbsp;I&nbsp; RUG CARE &nbsp;I&nbsp; FAQ &nbsp;I&nbsp; RETURN POLICY &nbsp;I&nbsp; FREE SHIPPING &nbsp;I&nbsp; CLEARANCE RUGS</div>
  <div class="copy">Copyright © 2013 LoomNest. All Rights Reserved.</div>
</footer>
</body>
</html>
```